Fable and Oat Mobile Bartending Website

Looking for an informational website for our mobile bartending business. We want to include features we like from another website that will help support our business.

Something with a similar set-up to https://wanderingtonicvan.example/

Coding

Coded - Design and coding required

```html
<!DOCTYPE html>
<html lang="en">
<head>
<meta charset="utf-8">
<title>Fable &amp; Oat Mobile Bartending</title>
<link href="https://fonts.googleapis.com/css2?family=Gilda+Display&family=Montserrat:wght@400;500;600;700&display=swap" rel="stylesheet">
<style>
:root{
  --taupe:#a38b7e;
  --peach:#ebc8b1;
  --peach-btn:#eec4aa;
  --ink:#2b2828;
  --ink-deep:#1f1d1d;
  --text:#4a4545;
  --white:#ffffff;
  --serif:"Gilda Display", Georgia, serif;
  --sans:"Montserrat", Arial, sans-serif;
}
*{box-sizing:border-box;margin:0;padding:0}
html,body{width:1200px;height:5235px;overflow:hidden}
body{position:relative;background:var(--white);font-family:var(--sans);color:var(--text)}
.abs{position:absolute}
.serif{font-family:var(--serif);font-weight:400}
.btn{position:absolute;display:flex;align-items:center;justify-content:center;font:700 9.5px var(--sans);letter-spacing:.5px;text-transform:uppercase;border-radius:4px}

/* top bar + nav */
.topbar{left:0;top:0;width:1200px;height:45px;background:var(--taupe)}
.topbar-item{position:absolute;top:12px;display:flex;align-items:center;gap:12px;color:#f3e8e1;font-size:9.5px;letter-spacing:.4px;line-height:20px}
.dot{width:20px;height:20px;border-radius:50%;background:#c9b5aa;display:inline-block}
.navbar{left:0;top:45px;width:1200px;height:67px;background:var(--white)}
.nav-link{position:absolute;top:72px;font-size:10px;color:var(--ink);letter-spacing:.3px}
.logo-tab{left:106px;top:0;width:185px;height:126px;background:var(--white);border-radius:0 0 40px 40px;display:flex;flex-direction:column;align-items:center;justify-content:center;gap:8px;box-shadow:0 6px 14px rgba(0,0,0,.06);z-index:2}
.logo-mark{width:22px;height:22px;border-radius:50%;background:var(--ink)}
.logo-name{font:600 24px var(--sans);color:var(--ink);letter-spacing:.5px;white-space:nowrap}

/* hero */
.hero{left:0;top:112px;width:1200px;height:680px;background:linear-gradient(100deg,#4b3e58 0%,#7a5a6a 30%,#b9806e 55%,#d7a07a 75%,#f0c9a0 100%)}
.hero-shade{left:0;top:112px;width:700px;height:680px;background:linear-gradient(90deg,rgba(40,30,45,.55),rgba(40,30,45,0))}
.hero-title{left:106px;top:268px;width:520px;font-size:40px;line-height:43px;color:var(--white);text-transform:uppercase}
.hero-copy{left:106px;top:408px;width:390px;font-size:11px;line-height:22.5px;color:var(--white)}

/* about */
.about-frame{left:126px;top:881px;width:452px;height:458px}
.about-photo{left:143px;top:900px;width:420px;height:425px;background:linear-gradient(135deg,#3b78a8 0%,#8fb6cf 35%,#c7a47d 60%,#5a4336 100%);border-bottom-right-radius:40px}
.h2{font-size:37px;color:#3d3838;text-transform:uppercase;letter-spacing:.5px}
.about-copy{left:655px;width:420px;font-size:11px;line-height:23px}

/* services */
.services{left:0;top:1458px;width:1200px;height:694px;background:var(--peach)}
.card{position:absolute;top:1680px;width:293px;height:293px;background:var(--white);border-radius:0 0 14px 0}
.card.active{background:var(--taupe)}
.card .num{position:absolute;right:28px;top:30px;font:64px var(--serif);color:var(--peach)}
.card.active .num{color:var(--white)}
.card svg.icon{position:absolute;left:32px;top:34px}
.card h3{position:absolute;left:32px;top:120px;font:700 14.5px var(--sans);color:var(--ink);text-transform:uppercase;letter-spacing:.3px}
.card p{position:absolute;left:32px;top:158px;width:228px;font-size:10px;line-height:21px}
.card .more{position:absolute;left:32px;top:250px;display:flex;align-items:center;gap:10px;font:700 10px var(--sans);color:var(--ink);text-transform:uppercase}
.card.active h3,.card.active .more{color:var(--white)}
.card.active p{color:#f2e6df}

/* testimonials */
.quote{position:absolute;border-radius:0 0 10px 10px;color:var(--white);text-align:center}
.quote.side{top:2366px;width:254px;height:227px;background:#b6a297;opacity:.75;font-size:9.5px;line-height:21px;padding:70px 20px 0}
.quote.main{left:452px;top:2355px;width:297px;height:267px;background:var(--ink);font-size:11px;line-height:24.5px;padding:80px 22px 0}
.qmark{position:absolute;font:150px/1 var(--serif);color:var(--peach)}
.arrow-btn{position:absolute;top:2465px;width:50px;height:50px;border-radius:50%}

/* cta */
.cta{left:0;top:2882px;width:1200px;height:470px;background:var(--taupe)}
.cta-title{left:134px;top:2962px;width:520px;font-size:38px;line-height:42px;color:var(--white);text-transform:uppercase}
.cta-copy{left:134px;top:3100px;width:460px;font-size:11px;line-height:23px;color:#f0e3da}
.cta-ring{left:722px;top:2884px;width:366px;height:366px;border-radius:50%;background:#c3a593}
.cta-person{left:690px;top:2756px;width:390px;height:596px;background:linear-gradient(180deg,#d9cbc1 0%,#f4f1ee 30%,#6a5e57 65%,#3c3532 100%);border-radius:180px 180px 0 0}

/* featured */
.press{position:absolute;width:310px;height:132px;background:var(--white);box-shadow:0 6px 22px rgba(0,0,0,.08);display:flex;align-items:center;justify-content:center;font:700 24px var(--sans);color:#3a3636}

/* follow */
.tile{position:absolute}
.insta-dot{left:240px;top:4290px;width:86px;height:86px;border-radius:50%;border:7px solid var(--white)}

/* footer */
.footer{left:0;top:4597px;width:1200px;height:638px;background:var(--ink)}
.foot-logo{left:130px;top:4745px;width:210px;display:flex;flex-direction:column;align-items:center;gap:8px}
.foot-copy{left:130px;top:4876px;width:285px;font-size:11px;line-height:26px;color:#e8e1dc}
.foot-h{font:15px var(--serif);color:var(--white);text-transform:uppercase;letter-spacing:.5px}
.foot-link{position:absolute;left:471px;font-size:12px;color:#e8e1dc}
.foot-social{position:absolute;top:5017px;width:30px;height:30px;border-radius:50%;background:var(--taupe)}
.contact{left:791px;top:4760px;width:301px;height:289px;background:var(--taupe);padding:40px 44px}
.c-row{position:absolute;display:flex;gap:16px;color:var(--white)}
.c-row small{display:block;font-size:7px;letter-spacing:.5px;margin-bottom:3px;opacity:.85}
.c-row span{font-size:9.5px;line-height:15px}
.copyright{left:0;top:5178px;width:1200px;height:57px;background:var(--ink-deep);display:flex;align-items:center;justify-content:center;font-size:11px;color:#e8e1dc;letter-spacing:.4px}
</style>
</head>
<body>

<!-- top bar -->
<div class="abs topbar"></div>
<div class="topbar-item" style="left:346px"><i class="dot"></i>ACCOUNT</div>
<div class="topbar-item" style="left:472px"><i class="dot"></i>CART CO.</div>
<div class="topbar-item" style="left:899px;font-weight:700;color:#fff">FOLLOW US ON:<i class="dot"></i></div>
<i class="dot abs" style="left:1040px;top:12px"></i><i class="dot abs" style="left:1072px;top:12px"></i>

<div class="abs navbar"></div>
<div class="abs logo-tab"><div class="logo-mark"></div><div class="logo-name">Fable &amp; Oat</div></div>
<a class="nav-link" style="left:344px">ABOUT US</a>
<a class="nav-link" style="left:445px">PACKAGES + BARS</a>
<a class="nav-link" style="left:590px">COCKTAIL MENU</a>
<a class="nav-link" style="left:724px">ALCOHOL CALCULATOR</a>
<div class="btn" style="left:899px;top:59px;width:195px;height:39px;background:var(--peach-btn);color:var(--white)">Schedule Consultation</div>

<!-- hero -->
<section class="abs hero" role="img" aria-label="Friends laughing and sharing drinks at a sunset party"></section>
<div class="abs hero-shade"></div>
<h1 class="abs serif hero-title">Shake it up with the best bartenders in town.</h1>
<p class="abs hero-copy">Lorem Ipsum is simply dummy text of the printing and typesetting industry. Lorem Ipsum has been the industry's standard dummy text ever since the 1500s, when an unknown printer took a galley of type and scrambled.</p>
<div class="btn" style="left:106px;top:533px;width:196px;height:37px;background:rgba(163,139,126,.8);color:var(--white)">Request our services</div>
<svg class="abs" style="left:0;top:700px" width="1200" height="100" viewBox="0 0 1200 100" preserveAspectRatio="none"><path d="M0 30 Q600 110 1200 20 L1200 100 L0 100Z" fill="#fff"/></svg>

<!-- about -->
<svg class="abs about-frame" viewBox="0 0 452 458"><path d="M2 458 V2 H204" fill="none" stroke="#ebc8b1" stroke-width="5"/><path d="M450 100 V410 Q450 456 404 456 H250" fill="none" stroke="#ebc8b1" stroke-width="5"/></svg>
<div class="abs about-photo" role="img" aria-label="Two men toasting with mint cocktails beside a mobile bar van"></div>
<h2 class="abs serif h2" style="left:655px;top:930px">About Us</h2>
<p class="abs about-copy" style="top:980px">Lorem Ipsum is simply dummy text of the printing and typesetting industry. Lorem Ipsum has been the industry's standard dummy text ever since the 1500s, when an unknown printer took a galley of type and scrambled it to make a type specimen book. It has survived not only five centuries.</p>
<p class="abs about-copy" style="top:1119px">but also the leap into electronic typesetting, remaining essentially unchanged. It was popularised in the 1960s with the release of Linotrace sheets containing Lorem Ipsum passages, and more recently with desktop publishing software like Quill LayoutDesk including versions of Lorem Ipsum.</p>
<div class="btn" style="left:655px;top:1266px;width:197px;height:36px;background:var(--peach-btn);color:var(--white)">Read more</div>

<!-- services -->
<section class="abs services"></section>
<h2 class="abs serif h2" style="left:0;top:1545px;width:1200px;text-align:center">Unique Bartending Services</h2>
<p class="abs" style="left:190px;top:1598px;width:820px;text-align:center;font-size:11px;line-height:24px">Lorem Ipsum is simply dummy text of the printing and typesetting industry. Lorem Ipsum has been the industry's standard dummy text ever since the 1500s, when an unknown printer took a galley of type.</p>

<div class="card active" style="left:134px">
<svg class="icon" width="60" height="60" viewBox="0 0 60 60" fill="none" stroke="#fff" stroke-width="2.5"><path d="M30 6 L52 18 V42 L30 54 L8 42 V18Z M8 18 L30 30 L52 18 M30 30 V54 M19 12 L41 24"/></svg>
<div class="num">01</div><h3>Packages + Bars</h3>
<p>Lorem Ipsum is simply dummy text of the printing and typesetting industry. Lorem Ipsum has been the industry's standard dummy text ever since the 1500s.</p>
<div class="more"><svg width="18" height="10"><path d="M0 5H16M11 1L16 5L11 9" stroke="#fff" stroke-width="1.5" fill="none"/></svg>More details</div></div>

<div class="card" style="left:454px">
<svg class="icon" width="64" height="64" viewBox="0 0 64 64" fill="none" stroke="#2b2828" stroke-width="3"><rect x="3" y="3" width="25" height="25" rx="6"/><rect x="36" y="3" width="25" height="25" rx="6"/><rect x="3" y="36" width="25" height="25" rx="6"/><rect x="36" y="36" width="25" height="25" rx="6"/></svg>
<div class="num">02</div><h3>Cocktail Menu</h3>
<p>Lorem Ipsum is simply dummy text of the printing and typesetting industry. Lorem Ipsum has been the industry's standard dummy text ever since the 1500s.</p>
<div class="more"><svg width="18" height="10"><path d="M0 5H16M11 1L16 5L11 9" stroke="#2b2828" stroke-width="1.5" fill="none"/></svg>More details</div></div>

<div class="card" style="left:773px">
<svg class="icon" width="52" height="60" viewBox="0 0 52 60" fill="none" stroke="#2b2828" stroke-width="3"><rect x="4" y="3" width="44" height="54" rx="5"/><rect x="12" y="11" width="28" height="12"/><g fill="#2b2828" stroke="none"><rect x="12" y="30" width="6" height="5"/><rect x="23" y="30" width="6" height="5"/><rect x="34" y="30" width="6" height="5"/><rect x="12" y="41" width="6" height="5"/><rect x="23" y="41" width="6" height="5"/><rect x="34" y="41" width="6" height="5"/></g></svg>
<div class="num">03</div><h3>Alcohol Calculator</h3>
<p>Lorem Ipsum is simply dummy text of the printing and typesetting industry. Lorem Ipsum has been the industry's standard dummy text ever since the 1500s.</p>
<div class="more"><svg width="18" height="10"><path d="M0 5H16M11 1L16 5L11 9" stroke="#2b2828" stroke-width="1.5" fill="none"/></svg>More details</div></div>

<div class="btn" style="left:502px;top:2020px;width:196px;height:36px;background:#3d3838;color:var(--white)">Request our services</div>

<!-- testimonials -->
<h2 class="abs serif h2" style="left:0;top:2240px;width:1200px;text-align:center">Testimonials</h2>
<div class="quote side" style="left:165px">Lorem Ipsum is simply dummy text of the printing and typesetting industry. Lorem Ipsum has been the industry's standard dummy text ever since the 1500s, when an unknown printer took</div>
<div class="quote side" style="left:781px">Lorem Ipsum is simply dummy text of the printing and typesetting industry. Lorem Ipsum has been the industry's standard dummy text ever since the 1500s, when an unknown printer took</div>
<div class="quote main">Lorem Ipsum is simply dummy text of the printing and typesetting industry. Lorem Ipsum has been the industry's standard dummy text ever since the 1500s, when an unknown printer took</div>
<div class="qmark" style="left:250px;top:2330px;opacity:.75">”</div>
<div class="qmark" style="left:866px;top:2330px;opacity:.75">”</div>
<div class="qmark" style="left:552px;top:2312px">”</div>
<div class="arrow-btn" style="left:73px;background:var(--taupe)"><svg width="50" height="50"><path d="M34 25H16M21 20L16 25L21 30" stroke="#fff" stroke-width="1.6" fill="none"/></svg></div>
<svg class="abs" style="left:128px;top:2482px" width="30" height="14"><path d="M30 7H4M9 2L4 7L9 12" stroke="#a38b7e" stroke-width="1.6" fill="none"/></svg>
<svg class="abs" style="left:1040px;top:2482px" width="30" height="14"><path d="M0 7H26M21 2L26 7L21 12" stroke="#a38b7e" stroke-width="1.6" fill="none"/></svg>
<div class="arrow-btn" style="left:1075px;background:#4a3f3c"><svg width="50" height="50"><path d="M16 25H34M29 20L34 25L29 30" stroke="#fff" stroke-width="1.6" fill="none"/></svg></div>
<div class="abs" role="img" aria-label="Client portrait" style="left:572px;top:2647px;width:56px;height:56px;border-radius:50%;background:linear-gradient(180deg,#e9e4e0,#cdbfb6);border:2px solid #f3ece7"></div>
<p class="abs" style="left:0;top:2720px;width:1200px;text-align:center;font:700 14px var(--sans);color:var(--ink)">MARISOL AVERY</p>
<p class="abs" style="left:0;top:2739px;width:1200px;text-align:center;font-size:10px;color:#8a8380">CEO</p>

<!-- cta -->
<section class="abs cta"></section>
<div class="abs cta-ring"></div>
<div class="abs cta-person" role="img" aria-label="Bartender in an apron holding a shaker and a blue cocktail"></div>
<h2 class="abs serif cta-title">Request our services<br>for your next<br>event!</h2>
<p class="abs cta-copy">Lorem Ipsum is simply dummy text of the printing and typesetting industry. Lorem Ipsum has been the industry's standard dummy text ever since the 1500s, when an unknown printer took a galley of type and scrambled it to make a type specimen book.</p>
<div class="btn" style="left:134px;top:3213px;width:196px;height:35px;background:var(--peach-btn);color:var(--white)">Schedule a consultation</div>

<!-- featured -->
<h2 class="abs serif h2" style="left:0;top:3440px;width:1200px;text-align:center">We're Featured In</h2>
<div class="press" style="left:118px;top:3533px">Harbor Daily</div>
<div class="press" style="left:443px;top:3533px">The Evening Ledger</div>
<div class="press" style="left:769px;top:3533px">Northline News</div>
<div class="press" style="left:118px;top:3688px">Fieldside Report</div>
<div class="press" style="left:443px;top:3688px">Coastal Wire</div>
<div class="press" style="left:769px;top:3688px">Summit Brief</div>

<!-- follow -->
<h2 class="abs serif h2" style="left:0;top:3906px;width:1200px;text-align:center">Follow Us On</h2>
<div class="tile" role="img" aria-label="Friends toasting with sparklers at a night party" style="left:134px;top:3989px;width:297px;height:163px;background:linear-gradient(135deg,#2a1c18,#8a4a2a,#e0a060)"></div>
<div class="tile" role="img" aria-label="Bartender mixing a drink behind the bar" style="left:134px;top:4170px;width:297px;height:326px;background:linear-gradient(160deg,#3a3432,#1e1a19)"></div>
<div class="abs insta-dot"></div>
<div class="tile" role="img" aria-label="Bartender straining an orange cocktail into a glass" style="left:452px;top:3989px;width:297px;height:327px;background:linear-gradient(180deg,#8a8785,#3d3a38 55%,#e0a540 80%,#403c3a)"></div>
<div class="tile" role="img" aria-label="Group of friends chatting over drinks" style="left:452px;top:4335px;width:297px;height:161px;background:linear-gradient(135deg,#6a4a3a,#c39070,#5a4030)"></div>
<div class="tile" role="img" aria-label="Bartender in a vest pouring a red drink" style="left:767px;top:3989px;width:297px;height:163px;background:linear-gradient(135deg,#f2f0ee,#5a5250 60%,#a04030)"></div>
<div class="tile" role="img" aria-label="Tray of pink cocktails with lime garnish" style="left:767px;top:4170px;width:297px;height:326px;background:linear-gradient(160deg,#5a2a5a,#c04a60 50%,#e68070 75%,#2a1e22)"></div>

<!-- footer -->
<section class="abs footer"></section>
<svg class="abs" style="left:0;top:4585px" width="1200" height="70" viewBox="0 0 1200 70" preserveAspectRatio="none"><path d="M0 0 H1200 V20 Q600 -15 0 60Z" fill="#fff"/></svg>
<div class="abs foot-logo"><div class="logo-mark" style="background:#fff"></div><div class="logo-name" style="color:#fff;font-size:27px">Fable &amp; Oat</div></div>
<p class="abs foot-copy">Lorem Ipsum is simply dummy text of the printing and typesetting industry. Lorem Ipsum has been the industry's standard dummy text ever since the 1500s, when an unknown printer took a galley of type and scrambled it to make a type specimen book.</p>
<h4 class="abs foot-h" style="left:471px;top:4762px">Quick Links</h4>
<a class="foot-link" style="top:4830px">Packages + Bars</a>
<a class="foot-link" style="top:4875px">Alcohol Calculator</a>
<a class="foot-link" style="top:4920px">Cocktail Menu</a>
<a class="foot-link" style="top:4965px">About Us</a>
<i class="foot-social" style="left:471px"></i>
<i class="foot-social" style="left:526px"></i>
<i class="foot-social" style="left:581px"></i>

<div class="abs contact"><h4 class="foot-h">Contact</h4></div>
<div class="c-row" style="left:835px;top:4832px"><svg width="18" height="14"><rect x="1" y="1" width="16" height="12" fill="none" stroke="#fff" stroke-width="1.6"/><path d="M1 1L9 8L17 1" stroke="#fff" stroke-width="1.6" fill="none"/></svg><div><small>MAIL</small><span>hello@fableandoat.example</span></div></div>
<div class="c-row" style="left:835px;top:4895px"><svg width="18" height="18"><path d="M2 8L17 1L10 17L8 10Z" fill="#fff"/></svg><div><small>ADDRESS</small><span>Fable &amp; Oat LLC, 48 Linden Row,<br>Ste 3, Millbrook, ST 00000</span></div></div>
<div class="c-row" style="left:835px;top:4970px"><svg width="18" height="18"><path d="M4 1L7 1L8 5L6 7Q8 11 11 12L13 10L17 11L17 14Q16 17 13 17Q2 14 1 4Q1 1 4 1Z" fill="#fff"/></svg><div><small>PHONE</small><span>(555) 014-2290</span></div></div>

<div class="abs copyright">© 2023 FABLE &amp; OAT LLC. ALL RIGHTS RESERVED.</div>
</body>
</html>
```